Company Values One-Pager

We're a recruitment firm based in Singapore, focused on the startup tech and VC sectors. www.brelvanhire.com

As we're now at the point of growing and hiring, we want a one-pager (PDF or whatever) that summarises us and our company values.

I've attached a short PowerPoint that goes into the values etc.

Font styles to use
Sans Serif

Requirements
Must have
• We like a 'clean' look. Our logo is bright and simple, and that's what we're looking for.
• The official colour code for the logo is seafoam green
• www.huepondlab.com/color/71EEB8/sea_foam_green
• Our website also gives a good insight.
• I'd like logos that summarise each value alongside them. i.e + for positivity, a letter for delivery etc. (Just ideas - please innovate!)
Should not have
• Nothing dark - just keep it simple and fresh

```html
<!DOCTYPE html>
<html lang="en">
<head>
<meta charset="utf-8">
<title>Brelvan Hire – Company Values One-Pager</title>
<link rel="stylesheet" href="https://fonts.googleapis.com/css2?family=Didact+Gothic&family=Titillium+Web:wght@400;600&display=swap">
<style>
  :root {
    --seafoam: #5fd39b;
    --seafoam-line: #71eeb8;
    --ink: #2f3436;
    --ink-soft: #5a6063;
    --paper: #f4f5f4;
    --white: #ffffff;
    --stage-top: #86a4a2;
    --stage-bottom: #bcd4d4;
    --hero-light: #e4f8ff;
    --hero-mid: #8fd4f0;
    --hero-edge: #4aa9dc;
  }
  * { box-sizing: border-box; margin: 0; padding: 0; }
  html, body { width: 1200px; height: 960px; overflow: hidden; }
  body {
    background: linear-gradient(180deg, var(--stage-top), var(--stage-bottom));
    font-family: "Didact Gothic", sans-serif;
    color: var(--ink);
    position: relative;
  }
  .sheet {
    position: absolute; left: 280px; top: 28px;
    width: 640px; height: 904px;
    background: var(--paper);
    box-shadow: 0 10px 30px rgba(30,50,50,.25);
    overflow: hidden;
  }
  .brand {
    position: absolute; left: 32px; top: 38px;
    display: flex; align-items: center; gap: 12px;
  }
  .brand-square { width: 18px; height: 18px; background: var(--seafoam); }
  .brand-name { font-size: 28px; font-weight: 400; letter-spacing: 4px; color: var(--seafoam); }
  .site-link {
    position: absolute; right: 38px; top: 40px;
    display: flex; align-items: center; gap: 10px;
    font-size: 15px; color: var(--ink);
  }
  .site-dot { width: 11px; height: 11px; border-radius: 50%; background: var(--seafoam); }
  .hero {
    position: absolute; left: 0; top: 96px; width: 640px; height: 282px;
    background: radial-gradient(ellipse at 35% 50%, var(--hero-light) 0%, var(--hero-mid) 40%, var(--hero-edge) 100%);
  }
  .hero-title {
    position: absolute; right: 14px; top: 96px;
    font-family: "Titillium Web", sans-serif; font-weight: 600;
    font-size: 44px; color: var(--white); letter-spacing: .5px;
  }
  .hero-note {
    position: absolute; right: 16px; top: 173px;
    font-size: 13px; color: var(--white);
  }
  .tagline {
    position: absolute; left: 95px; top: 350px; width: 453px; height: 59px;
    background: var(--seafoam); color: var(--white); text-align: center;
    padding-top: 6px; line-height: 1.1;
  }
  .tagline-main { font-size: 21px; }
  .tagline-sub { font-size: 16px; }
  .column { position: absolute; top: 464px; }
  .column-who { left: 34px; width: 200px; }
  .column-values { left: 258px; width: 352px; }
  .section-title {
    font-size: 25px; font-weight: 400; letter-spacing: .5px; color: var(--ink);
    padding-bottom: 4px; border-bottom: 1px solid var(--seafoam);
    position: relative; margin-bottom: 20px; width: 100%;
  }
  .section-title::after {
    content: ""; position: absolute; left: 50%; bottom: -5px;
    border: 4px solid transparent; border-top-color: var(--seafoam);
    border-bottom: 0; transform: translateX(-50%);
  }
  .fact { margin-bottom: 19px; }
  .fact-label {
    font-size: 12.5px; padding-left: 12px; position: relative; margin-bottom: 5px;
  }
  .fact-label::before {
    content: ""; position: absolute; left: 0; top: 2px;
    width: 2px; height: 10px; background: var(--seafoam);
  }
  .fact-text { font-size: 10px; line-height: 1.35; color: var(--ink-soft); }
  .value { display: flex; gap: 10px; margin-bottom: 22px; }
  .value-icon { flex: 0 0 26px; width: 26px; height: 26px; }
  .value-body { min-width: 0; }
  .value-head {
    display: inline-flex; align-items: baseline; gap: 7px; white-space: nowrap;
    border-bottom: 1px solid var(--seafoam-line); padding-bottom: 2px; margin-bottom: 7px;
  }
  .value-name { font-size: 13.5px; color: var(--seafoam); letter-spacing: .3px; }
  .value-def { font-size: 9.5px; color: var(--ink); }
  .value-text { font-size: 10px; line-height: 1.35; color: var(--ink-soft); }
  .contact-bar {
    position: absolute; left: 16px; right: 16px; top: 862px;
    display: flex; justify-content: space-between;
    font-size: 9.5px; color: var(--ink-soft);
  }
  .contact-item { display: flex; align-items: center; gap: 5px; }
  .contact-item svg { width: 11px; height: 11px; }
  .base-line {
    position: absolute; left: 0; bottom: 0; width: 100%; height: 5px;
    background: var(--seafoam);
  }
</style>
</head>
<body>
  <main class="sheet">
    <div class="brand">
      <span class="brand-square"></span>
      <span class="brand-name">BRELVAN HIRE</span>
    </div>
    <div class="site-link"><span class="site-dot"></span>www.brelvanhire.com</div>

    <div class="hero" role="img" aria-label="Photo of a businessman touching a glowing hexagon search icon over a light blue circuit-board background"></div>
    <div class="hero-title">CORE VALUES</div>
    <div class="hero-note">search completed</div>

    <div class="tagline">
      <div class="tagline-main">THE RECRUITMENT PARTNER FOR THE</div>
      <div class="tagline-sub">SOUTH-EAST ASIA STARTUP ECOSYSTEM</div>
    </div>

    <section class="column column-who">
      <h2 class="section-title">WHO WE ARE</h2>
      <div class="fact">
        <div class="fact-label">WHAT</div>
        <p class="fact-text">We are the ‘recruitment partner for the startup ecosystem in South-East Asia’; partnering with Venture Capital and startup tech firms, HQ’d out of Singapore.</p>
      </div>
      <div class="fact">
        <div class="fact-label">WHO</div>
        <p class="fact-text">Established by Dara Lim &amp; Owen Fairley</p>
      </div>
      <div class="fact">
        <div class="fact-label">WHEN</div>
        <p class="fact-text">Opened our doors in September 2016</p>
      </div>
      <div class="fact">
        <div class="fact-label">LONGER-TERM GOAL</div>
        <p class="fact-text">Asia and Global expansion</p>
      </div>
      <div class="fact">
        <div class="fact-label">CORE VALUES</div>
        <p class="fact-text">Positivity - Proactivity - Teamwork - Delivery</p>
      </div>
    </section>

    <section class="column column-values">
      <h2 class="section-title">OUR CORE VALUES</h2>
      <div class="value">
        <svg class="value-icon" viewBox="0 0 26 26" aria-hidden="true"><circle cx="13" cy="13" r="13" fill="#5fd39b"/><path d="M13 7v12M7 13h12" stroke="#fff" stroke-width="2.4" stroke-linecap="round"/></svg>
        <div class="value-body">
          <div class="value-head"><span class="value-name">POSITIVITY</span><span class="value-def">the character of being positive</span></div>
          <p class="value-text">We look on the bright side…<br>and don’t let limiting beliefs hold us back</p>
        </div>
      </div>
      <div class="value">
        <svg class="value-icon" viewBox="0 0 26 26" aria-hidden="true"><circle cx="13" cy="13" r="13" fill="#5fd39b"/><path d="M7 13h11M14 8.5l4.5 4.5-4.5 4.5" fill="none" stroke="#fff" stroke-width="2.4" stroke-linecap="round" stroke-linejoin="round"/></svg>
        <div class="value-body">
          <div class="value-head"><span class="value-name">PROACTIVITY</span><span class="value-def">to initiate change rather than reacting to events</span></div>
          <p class="value-text">We dont wait… we make things happen</p>
        </div>
      </div>
      <div class="value">
        <svg class="value-icon" viewBox="0 0 26 26" aria-hidden="true"><circle cx="13" cy="13" r="13" fill="#5fd39b"/><circle cx="10" cy="13" r="4.2" fill="none" stroke="#fff" stroke-width="2"/><circle cx="16" cy="13" r="4.2" fill="none" stroke="#fff" stroke-width="2"/></svg>
        <div class="value-body">
          <div class="value-head"><span class="value-name">TEAMWORK</span><span class="value-def">working together</span></div>
          <p class="value-text">We work together… to solve problems,<br>find solutions, and celebrate the good times</p>
        </div>
      </div>
      <div class="value">
        <svg class="value-icon" viewBox="0 0 26 26" aria-hidden="true"><circle cx="13" cy="13" r="13" fill="#5fd39b"/><path d="M7.5 13.5l3.8 3.8 7.2-8" fill="none" stroke="#fff" stroke-width="2.4" stroke-linecap="round" stroke-linejoin="round"/></svg>
        <div class="value-body">
          <div class="value-head"><span class="value-name">DELIVERY</span><span class="value-def">to achieve what is desired, expected or promised</span></div>
          <p class="value-text">We do what we say we’re going to do…<br>for our candidates, clients, and colleagues alike</p>
        </div>
      </div>
    </section>

    <footer class="contact-bar">
      <span class="contact-item">
        <svg viewBox="0 0 12 12"><rect x=".5" y=".5" width="11" height="11" fill="none" stroke="#5a6063"/><path d="M6 2.5a2 2 0 0 1 2 2c0 1.5-2 4-2 4s-2-2.5-2-4a2 2 0 0 1 2-2z" fill="#5a6063"/></svg>
        48 Tessel Road, Marlow House, #05-02, Singapore 068211
      </span>
      <span class="contact-item">
        <svg viewBox="0 0 12 12"><rect x=".5" y=".5" width="11" height="11" fill="none" stroke="#5a6063"/><rect x="3" y="4" width="6" height="4" fill="#5a6063"/></svg>
        +65 6204 8835
      </span>
      <span class="contact-item">
        <svg viewBox="0 0 12 12"><rect x=".5" y=".5" width="11" height="11" fill="none" stroke="#5a6063"/><path d="M2.5 4h7v4.5h-7zM2.5 4l3.5 2.5L9.5 4" fill="none" stroke="#5a6063"/></svg>
        info@brelvanhire.com
      </span>
      <span class="contact-item">
        <svg viewBox="0 0 12 12"><rect x=".5" y=".5" width="11" height="11" fill="none" stroke="#5a6063"/><circle cx="6" cy="6" r="3" fill="none" stroke="#5a6063"/></svg>
        www.brelvanhire.com
      </span>
    </footer>
    <div class="base-line"></div>
  </main>
</body>
</html>
```